Label for packaging - front and back

Hello,
We are looking for a fresh design based off of the current one we have. We need something fresh simple and eye catching. Company is MeadowGlint.com I am including current packaging and also a trim fold fliers we had made.
MG Brochure is what we could use as design inspiration perhaps?
Updates
PLEASE replace super food with " Beyond Super Food". somewhere on the label. In addition, please include website name on front.
Target Market(s)
Nutrition, athletes, anyone who wants to improve health
Look and feel
Each slider illustrates characteristics of the customer's brand and the style your logo design should communicate.

```html
<!DOCTYPE html>
<html lang="en">
<head>
<meta charset="UTF-8">
<title>MeadowGlint – Live Spirulina Pouch Label</title>
<link href="https://fonts.googleapis.com/css2?family=Josefin+Sans:wght@400&family=Josefin+Slab:wght@300&family=Open+Sans:wght@400&display=swap" rel="stylesheet">
<style>
  :root {
    --bg: #d5dadc;
    --white: #ffffff;
    --teal: #3fb591;
    --teal-light: #6fcdb0;
    --green-deep: #1d5e43;
    --green-mid: #2e7a59;
    --green-powder: #3d8a66;
    --green-powder-light: #5b9f80;
    --rim: #e3e8e5;
    --navy: #1d2a3a;
    --headline: #2fa86f;
    --zip: #e6e9ea;
  }
  * { margin: 0; padding: 0; box-sizing: border-box; }
  html, body {
    width: 1200px;
    height: 835px;
    overflow: hidden;
    background: var(--bg);
  }
  .canvas {
    position: relative;
    width: 1200px;
    height: 835px;
  }
  .pouch-label {
    position: absolute;
    left: 378px;
    top: 25px;
    width: 444px;
    height: 785px;
    background: var(--white);
    border-radius: 14px 14px 4px 4px;
    overflow: hidden;
  }
  .top-band {
    position: absolute;
    left: 0; top: 0;
    width: 100%;
    height: 18px;
    background: linear-gradient(90deg, var(--teal), var(--teal-light));
  }
  .zip-line {
    position: absolute;
    left: 22px;
    right: 22px;
    height: 2px;
    background: var(--zip);
  }
  .zip-line.upper { top: 78px; }
  .zip-line.lower { top: 94px; height: 6px; }
  .brand {
    position: absolute;
    left: 0;
    top: 160px;
    width: 100%;
    display: flex;
    align-items: center;
    justify-content: center;
    gap: 14px;
  }
  .brand-dot {
    width: 40px;
    height: 40px;
    border-radius: 50%;
    background: var(--teal);
  }
  .brand-name {
    font-family: "Josefin Sans", sans-serif;
    font-weight: 400;
    font-size: 26px;
    letter-spacing: 2px;
    color: var(--navy);
  }
  .headline {
    position: absolute;
    left: 0;
    width: 100%;
    text-align: center;
    font-family: "Josefin Slab", serif;
    font-weight: 300;
    color: var(--headline);
  }
  .headline.primary { top: 258px; font-size: 40px; letter-spacing: 0.5px; }
  .headline.secondary { top: 314px; font-size: 28px; }
  .product-photo {
    position: absolute;
    left: 0;
    top: 355px;
    width: 100%;
    height: 430px;
    background:
      radial-gradient(circle 160px at 49% 44%,
        var(--green-powder-light) 0%,
        var(--green-powder) 55%,
        #35805e 88%,
        var(--rim) 92%,
        #f1f4f2 95%,
        rgba(255,255,255,0) 100%),
      radial-gradient(ellipse 70% 40% at 20% 70%, rgba(20,80,55,0.55), rgba(20,80,55,0) 100%),
      linear-gradient(180deg, rgba(255,255,255,1) 0%, rgba(150,190,170,0.6) 12%, var(--green-mid) 45%, var(--green-deep) 100%);
  }
  .badge-shape {
    position: absolute;
    left: 293px;
    top: 388px;
    width: 88px;
    height: 88px;
    border-radius: 50%;
    background: var(--teal);
    border: 4px solid var(--white);
  }
  .website-pill {
    position: absolute;
    left: 107px;
    top: 740px;
    width: 220px;
    height: 28px;
    border-radius: 14px;
    background: var(--teal);
    display: flex;
    align-items: center;
    justify-content: center;
    font-family: "Open Sans", sans-serif;
    font-size: 15px;
    color: var(--white);
  }
  .weight-circle {
    position: absolute;
    left: 335px;
    top: 703px;
    width: 88px;
    height: 88px;
    border-radius: 50%;
    background: rgba(111, 205, 176, 0.85);
    display: flex;
    align-items: center;
    justify-content: center;
    font-family: "Open Sans", sans-serif;
    font-size: 18px;
    color: var(--white);
  }
</style>
</head>
<body>
<main class="canvas">
  <section class="pouch-label">
    <div class="top-band"></div>
    <div class="zip-line upper"></div>
    <div class="zip-line lower"></div>

    <div class="brand">
      <span class="brand-dot"></span>
      <span class="brand-name">MeadowGlint</span>
    </div>

    <h1 class="headline primary">LIVE SPIRULINA</h1>
    <h2 class="headline secondary">BEYOND SUPER FOOD</h2>

    <div class="product-photo" role="img" aria-label="Glass bowl filled with green spirulina powder, loose powder scattered around it"></div>
    <div class="badge-shape"></div>

    <div class="website-pill">www.meadowglint.com</div>
    <div class="weight-circle">450 g</div>
  </section>
</main>
</body>
</html>
```